Personal Motivational Quote Poster Design

I would like to create a poster with some of my favorite quotes to hang in my office. I did similar projects in 2012 and 2014. I've uploaded the winning designs so you can get a better idea of what I'm looking for. I will provide feedback on your design within 24 hours of receiving it.

The poster must contain the following quotes:

“What the pupil must learn, if he learns anything at all, is that the world will do most of the work for you, provided you cooperate with it by identifying how it really works and aligning with those realities. If we do not let the world teach us, it teaches us a lesson.” - Harold Wexbury

“I tackle every big new problem by asking two questions: Who has dealt with this problem well? And what can we learn from them?” - Tom Harlow

“If we can really understand the problem, the answer will come out of it, because the answer is not separate from the problem.” - Ravindra Pallathuri

“Success is nothing more than a few simple disciplines, practiced every day; while failure is simply a few errors in judgment, repeated every day. It is the accumulative weight of our disciplines and our judgments that leads us to either fortune or failure.” - Ned Pilsk

“Inaction breeds doubt and fear. Action breeds confidence and courage.” - Walt Brimsley

“What’s the one thing you can do, such that by doing it, everything else will be easier or unnecessary?” - Lenny Druse

Requirements
Must have
• The poster will be 24" high x 36" long and printed on canvas, so the image you create needs to have a resolution of at least 2700 x 3900.
Nice to have
• I don't have an exact vision for how the poster should look, so I am totally open to you using your creativity to develop, arrange and present the content as you'd like.

That said, I would like an image (photo or posterized image) of the person being quoted along with each quote. I do not have specific images that I would like you to use, so you will need to find the images on your own.

The images don't need to be perfect... I am more interested in the poster relating the essence of the quotes and the people being quoted than I am in perfect photographic images of the people being quoted.

```html
<!DOCTYPE html>
<html lang="en">
<head>
<meta charset="utf-8">
<title>Quote Poster</title>
<link rel="stylesheet" href="https://fonts.googleapis.com/css2?family=PT+Sans&family=Didact+Gothic&family=Allura&display=swap">
<style>
  :root {
    --page: #d9d6d8;
    --navy: #071a3f;
    --blue: #0d56b8;
    --blue-bright: #1f78e0;
    --grid: rgba(140, 190, 255, 0.28);
    --paper: #ffffff;
    --ink: #1b1b1b;
    --portrait-light: #eceff3;
    --portrait-dark: #c9ced6;
  }
  * { box-sizing: border-box; margin: 0; padding: 0; }
  html, body { width: 988px; height: 1200px; overflow: hidden; background: var(--page); }
  .canvas { position: relative; width: 988px; height: 1200px; }
  .poster {
    position: absolute; left: 142px; top: 21px; width: 741px; height: 1104px;
    background:
      repeating-linear-gradient(90deg, var(--grid) 0 1px, transparent 1px 48px),
      repeating-linear-gradient(0deg, var(--grid) 0 1px, transparent 1px 48px),
      radial-gradient(ellipse at 55% 50%, var(--blue-bright) 0%, var(--blue) 40%, var(--navy) 100%);
    box-shadow: 0 4px 14px rgba(0,0,0,0.35);
    overflow: hidden;
  }
  .quote-card {
    position: absolute; background: var(--paper);
    border-radius: 26px 18px 30px 16px;
  }
  .quote-card::after {
    content: ""; position: absolute; inset: -8px -7px -8px -9px;
    border: 2px solid var(--paper); border-radius: 30px 22px 34px 20px;
  }
  .quote-text { position: absolute; color: var(--ink); white-space: nowrap; }
  .quote-text--sans { font-family: "PT Sans", sans-serif; }
  .quote-text--round { font-family: "Didact Gothic", sans-serif; }
  .author {
    position: absolute; font-family: "Allura", cursive; font-size: 25px; color: var(--ink); white-space: nowrap;
  }
  .portrait {
    position: absolute; border-radius: 12px;
    background: radial-gradient(ellipse at 50% 40%, var(--portrait-light) 0%, var(--portrait-dark) 100%);
  }
</style>
</head>
<body>
<div class="canvas">
  <div class="poster">

    <div class="quote-card" style="left:32px;top:16px;width:690px;height:224px;"></div>
    <p class="quote-text quote-text--sans" style="left:46px;top:28px;font-size:18px;line-height:26.5px;">“What the pupil must learn, if he learns anything at all,<br>is that the world will do most of the work for you,<br>provided you cooperate with it by identifying how<br>it really works and aligning with those realities.<br>If we do not let the world teach us, it teaches<br>us a lesson.”</p>
    <div class="portrait" role="img" aria-label="Sketched portrait of Harold Wexbury" style="left:530px;top:34px;width:180px;height:196px;"></div>
    <span class="author" style="left:335px;top:196px;">Harold Wexbury</span>

    <div class="quote-card" style="left:73px;top:260px;width:645px;height:148px;"></div>
    <div class="portrait" role="img" aria-label="Sketched portrait of Tom Harlow" style="left:84px;top:268px;width:104px;height:132px;"></div>
    <p class="quote-text quote-text--round" style="left:198px;top:292px;font-size:19px;line-height:28px;">“I tackle every big new problem by asking two<br>questions: Who has dealt with this problem<br>well? And what can we learn from them?”</p>
    <span class="author" style="left:207px;top:380px;">Tom Harlow</span>

    <div class="quote-card" style="left:35px;top:444px;width:660px;height:134px;"></div>
    <p class="quote-text quote-text--sans" style="left:56px;top:462px;font-size:18px;line-height:28px;">“If we can really understand the problem, the answer<br>will come out of it, because the answer is not<br>separate from the problem.”</p>
    <div class="portrait" role="img" aria-label="Sketched portrait of Ravindra Pallathuri" style="left:540px;top:451px;width:146px;height:120px;"></div>
    <span class="author" style="left:330px;top:538px;">Ravindra Pallathuri</span>

    <div class="quote-card" style="left:33px;top:596px;width:686px;height:196px;"></div>
    <div class="portrait" role="img" aria-label="Sketched portrait of Ned Pilsk" style="left:42px;top:604px;width:142px;height:180px;"></div>
    <p class="quote-text quote-text--round" style="left:193px;top:607px;font-size:17px;line-height:27px;">“Success is nothing more than a few simple disciplines,<br>practiced every day; while failure is simply a few<br>errors in judgment, repeated every day. It is the<br>accumulative weight of our disciplines and our<br>judgments that leads us to either fortune or failure.”</p>
    <span class="author" style="left:196px;top:748px;">Ned Pilsk</span>

    <div class="quote-card" style="left:91px;top:806px;width:610px;height:136px;"></div>
    <p class="quote-text quote-text--sans" style="left:111px;top:832px;font-size:18.5px;line-height:26px;">“Inaction breeds doubt and fear.<br>&nbsp;Action breeds confidence and courage.”</p>
    <div class="portrait" role="img" aria-label="Sketched portrait of Walt Brimsley" style="left:520px;top:814px;width:166px;height:120px;"></div>
    <span class="author" style="left:360px;top:900px;">Walt Brimsley</span>

    <div class="quote-card" style="left:30px;top:956px;width:694px;height:128px;"></div>
    <div class="portrait" role="img" aria-label="Sketched portrait of Lenny Druse" style="left:38px;top:964px;width:104px;height:112px;"></div>
    <p class="quote-text quote-text--round" style="left:158px;top:981px;font-size:18px;line-height:27px;">“What’s the one thing you can do, such that by doing it,<br>everything else will be easier or unnecessary?”</p>
    <span class="author" style="left:176px;top:1040px;">Lenny Druse</span>

  </div>
</div>
</body>
</html>
```